Fabric Store Business card

Need a business card portraying store logo and up and coming business of quilt fabrics, apparel fabrics, notions and buttons. Our business name is Gilded Thimble and Such. Am attaching logo. The design should communicate a growing business and warm atmosphere. Would like address and store hours and contact info displayed on card. Mon - Fri 9:30 to 5:00, Saturday 9:30 to 1:00. Address 287 W Alder Ave, Newton, KS 67392 email: gildedthimbleandsuch@mailbrook.net. Phone and fax 316-555-2846. After hours contact # 620-555-3914 Also like vintage sewing machines and dress forms if it works to incorporate fine, if not thats ok too.

```html
<!DOCTYPE html>
<html lang="en">
<head>
<meta charset="utf-8">
<title>Gilded Thimble and Such — Business Card</title>
<link rel="stylesheet" href="https://fonts.googleapis.com/css2?family=Libre+Baskerville:wght@400;700&family=Pinyon+Script&display=swap">
<style>
  :root {
    --stage-top: #0c0c0c;
    --stage-mid: #4a4a4a;
    --cloth-red: #8f1b26;
    --cloth-red-dark: #7a1520;
    --label-white: #ffffff;
    --thread-light: #e8e8e8;
    --thread-dark: #555555;
    --ink: #1e1e1e;
    --accent-red: #9b1c27;
  }
  * { box-sizing: border-box; margin: 0; padding: 0; }
  html, body { width: 1200px; height: 1000px; overflow: hidden; }
  body {
    position: relative;
    background: linear-gradient(180deg, var(--stage-top) 0%, var(--stage-mid) 50%, var(--stage-top) 100%);
    font-family: "Libre Baskerville", Georgia, serif;
    color: var(--ink);
  }
  .card {
    position: absolute;
    left: 258px;
    width: 680px;
    height: 387px;
    background: radial-gradient(ellipse at center, var(--cloth-red) 0%, var(--cloth-red-dark) 100%);
    box-shadow: 0 4px 14px rgba(0,0,0,0.5);
  }
  .card--front { top: 91px; }
  .card--back { top: 517px; }
  .card__stitch {
    position: absolute;
    inset: 12px;
    border: 2px dashed var(--thread-light);
  }
  .label {
    position: absolute;
    left: 111px;
    width: 459px;
    background: var(--label-white);
    box-shadow: 0 1px 3px rgba(0,0,0,0.35);
  }
  .label__stitch {
    position: absolute;
    inset: 7px;
    border: 2px dashed var(--thread-dark);
  }
  .card--front .label { top: 107px; height: 170px; }
  .card--back .label { top: 63px; height: 263px; }

  .brand {
    position: absolute;
    inset: 0;
    display: flex;
    align-items: center;
    justify-content: center;
    gap: 12px;
    padding: 0 30px;
  }
  .brand__dot {
    width: 60px; height: 60px;
    border-radius: 50%;
    background: var(--accent-red);
    flex: none;
  }
  .brand__name {
    font-family: "Pinyon Script", cursive;
    font-size: 31px;
    line-height: 1;
    color: var(--accent-red);
    white-space: nowrap;
  }

  .details {
    position: absolute;
    inset: 0;
    text-align: center;
    padding-top: 24px;
  }
  .script {
    font-family: "Pinyon Script", cursive;
    color: var(--accent-red);
  }
  .details__label { font-size: 27px; line-height: 32px; }
  .details__address { font-size: 20px; line-height: 32px; }
  .details__hours {
    margin-top: 10px;
    font-weight: 700;
    font-size: 21px;
    line-height: 30px;
    color: var(--accent-red);
  }
  .details__phones {
    margin-top: 14px;
    font-size: 19px;
    line-height: 28px;
  }
  .details__phones .script { font-size: 26px; }
  .details__phones .gap { display: inline-block; width: 18px; }
  .details__email {
    margin-top: 6px;
    font-size: 15px;
    line-height: 24px;
  }
  .details__email .script { font-size: 22px; }
</style>
</head>
<body>
  <section class="card card--front" aria-label="Business card front">
    <div class="card__stitch"></div>
    <div class="label">
      <div class="label__stitch"></div>
      <div class="brand">
        <span class="brand__dot"></span>
        <span class="brand__name">Gilded Thimble and Such</span>
      </div>
    </div>
  </section>

  <section class="card card--back" aria-label="Business card back">
    <div class="card__stitch"></div>
    <div class="label">
      <div class="label__stitch"></div>
      <div class="details">
        <p class="details__label script">Address:</p>
        <p class="details__address">287 W Alder Ave, Newton, KS 67392</p>
        <p class="details__hours">MON - FRI&nbsp; 9:30 TO 5:00<br>SATURDAY 9:30 TO 1:00</p>
        <p class="details__phones"><span class="script">f:</span>316-555-2846<span class="gap"></span><span class="script">p:</span>620-555-3914</p>
        <p class="details__email"><span class="script">e:</span> gildedthimbleandsuch@mailbrook.net</p>
      </div>
    </div>
  </section>
</body>
</html>
```